Unique, Impressive, and Modern Business Card

Looking for a distinctive, unique business card. We are distributors of tire repairs supplies, tools, machinery, and chemicals. Our target market are tire repair shops, tire franchises, and mechanic shops. We would like our design to include tire characteristics, and use our business colors. Feel free to use all types design and printing options (emboss, spot uv, foil, etc) QR code may be applied, you can use different size business cards ( standard, square, rounded edge, colored edge, etc), all formats needed for printing, also editable for future changes

Target Market(s)

Automotive, Tire industries

Industry/Entity Type

Tire Industry (automotive)

Contact Information for Business Card

Business logo, business Name (Corvane Supply Inc), Name (Marcus Pellow), Position (President) Address (58 Fernhollow Lane, Brentwood NY 11742), Contact number (Company 1-855-302-4418, Cell 1-631-245-9073, email address (marcus.pellow@corvanesupply.com), URL (www.corvanesupply.com

Requirements
Must have
• Must include Business Colors (Black, Green, Blue, White) see sample website file
Nice to have
• emboss, spot uv, etc

```html
<!DOCTYPE html>
<html lang="en">
<head>
<meta charset="utf-8">
<title>Corvane Supply Inc – Business Card</title>
<link rel="stylesheet" href="https://fonts.googleapis.com/css2?family=Montserrat:wght@400;500&family=Roboto:wght@500;700&display=swap">
<style>
  :root {
    --stage: #e6e7e9;
    --paper: #f7f7f8;
    --ink: #111111;
    --text: #3a3a3a;
    --brand-blue: #0a5fd6;
    --brand-blue-deep: #0047a8;
    --brand-blue-light: #0a6ff2;
    --brand-green: #22d42a;
    --mark-blue: #0a18d8;
    --card-dark: #231f20;
    --tread-light: #dedfe1;
    --tread-dark: #3a3839;
  }
  * { box-sizing: border-box; margin: 0; padding: 0; }
  html, body { width: 1200px; height: 1200px; overflow: hidden; }
  body { background: var(--stage); position: relative; font-family: "Montserrat", sans-serif; }

  .card {
    position: absolute; left: 204px; width: 792px; height: 454px;
    border-radius: 36px; overflow: hidden;
    box-shadow: 0 6px 18px rgba(0,0,0,.18);
  }
  .card-front { top: 102px; background: var(--paper); }
  .card-back { top: 644px; background: var(--card-dark); }

  .swoosh { position: absolute; inset: 0; width: 100%; height: 100%; }

  .tread-front {
    position: absolute; left: 0; top: 0; width: 410px; height: 454px;
    background: radial-gradient(ellipse 60% 70% at 20% 50%, rgba(222,223,225,0) 40%, var(--tread-light) 62%, rgba(222,223,225,0) 100%);
  }
  .tread-back {
    position: absolute; left: 384px; top: 30px; width: 408px; height: 424px;
    border-radius: 200px 0 0 200px;
    background: linear-gradient(90deg, rgba(58,56,57,0) 0%, var(--tread-dark) 55%, #2c2a2b 100%);
  }

  .brand { position: absolute; left: 22px; top: 48px; display: flex; align-items: center; gap: 10px; }
  .brand-dot { width: 20px; height: 20px; border-radius: 50%; background: var(--mark-blue); }
  .brand-name {
    font-family: "Roboto", sans-serif; font-weight: 700; font-size: 26px;
    color: var(--ink); letter-spacing: .02em; line-height: 1.05;
  }

  .person { position: absolute; left: 19px; top: 218px; }
  .person-name {
    font-family: "Roboto", sans-serif; font-weight: 700; font-size: 32px;
    letter-spacing: .14em; color: var(--ink); line-height: 1;
  }
  .person-role {
    margin-top: 10px; font-family: "Roboto", sans-serif; font-weight: 700; font-size: 15px;
    letter-spacing: .42em; color: var(--ink);
  }
  .person-rule { margin-top: 6px; width: 250px; height: 4px; background: var(--brand-blue); }

  .address {
    position: absolute; left: 19px; top: 314px;
    font-size: 18px; line-height: 24px; color: var(--text);
  }

  .contacts { position: absolute; left: 408px; top: 226px; list-style: none; }
  .contact { display: flex; align-items: flex-start; gap: 22px; font-size: 18px; line-height: 22px; color: var(--text); margin-bottom: 14px; }
  .contact:nth-child(2) { margin-bottom: 22px; }
  .contact svg { width: 24px; height: 24px; flex: none; margin-top: 6px; fill: var(--mark-blue); }

  .back-brand {
    position: absolute; left: 0; right: 0; top: 190px;
    display: flex; justify-content: center; align-items: center; gap: 16px;
  }
  .back-brand .brand-dot { width: 46px; height: 46px; }
  .back-brand .brand-name { color: #ffffff; font-size: 54px; }
</style>
</head>
<body>

<section class="card card-front" aria-label="Business card front">
  <div class="tread-front" role="img" aria-label="Faint stacked tire tread decoration"></div>
  <svg class="swoosh" viewBox="0 0 792 454" aria-hidden="true">
    <defs>
      <linearGradient id="blueFront" x1="0" y1="0" x2="1" y2="0">
        <stop offset="0" stop-color="var(--brand-blue-deep)"/>
        <stop offset="1" stop-color="var(--brand-blue-light)"/>
      </linearGradient>
    </defs>
    <path d="M200 0 Q600 30 792 306 L792 0 Z" fill="url(#blueFront)"/>
    <path d="M370 40 Q700 140 792 440 L792 392 Q690 130 370 40 Z" fill="var(--brand-green)"/>
  </svg>

  <div class="brand">
    <span class="brand-dot"></span>
    <span class="brand-name">CORVANE<br>SUPPLY</span>
  </div>

  <div class="person">
    <h1 class="person-name">Marcus Pellow</h1>
    <p class="person-role">PRESIDENT</p>
    <div class="person-rule"></div>
  </div>

  <address class="address" style="font-style:normal">58 Fernhollow Lane,<br>Brentwood<br>NY 11742</address>

  <ul class="contacts">
    <li class="contact">
      <svg viewBox="0 0 24 24" aria-hidden="true"><path d="M2 3 L22 12 L2 21 L6 12 Z"/></svg>
      <span>marcus.pellow@<br>&nbsp;&nbsp;&nbsp;&nbsp;&nbsp;&nbsp;&nbsp;corvanesupply.com</span>
    </li>
    <li class="contact">
      <svg viewBox="0 0 24 24" aria-hidden="true"><path d="M2 9 Q12 2 22 9 L20 12 L16 10 L16 8 Q12 6 8 8 L8 10 L4 12 Z M5 13 H19 V21 H5 Z"/></svg>
      <span>+1-855-302-4418<br>+1-631-245-9073</span>
    </li>
    <li class="contact">
      <svg viewBox="0 0 24 24" aria-hidden="true"><circle cx="12" cy="12" r="10"/></svg>
      <span>www.corvanesupply.com</span>
    </li>
  </ul>
</section>

<section class="card card-back" aria-label="Business card back">
  <div class="tread-back" role="img" aria-label="Dark stacked tire tread decoration"></div>
  <svg class="swoosh" viewBox="0 0 792 454" aria-hidden="true">
    <defs>
      <linearGradient id="blueBack" x1="0" y1="0" x2="1" y2="0">
        <stop offset="0" stop-color="var(--brand-blue-deep)"/>
        <stop offset="1" stop-color="var(--brand-blue)"/>
      </linearGradient>
    </defs>
    <path d="M0 0 L300 0 Q90 60 0 215 Z" fill="#ffffff"/>
    <path d="M0 0 L226 0 Q60 70 0 232 Z" fill="url(#blueBack)"/>
    <path d="M300 0 L310 0 Q80 60 0 250 L0 215 Q90 60 300 0 Z" fill="var(--brand-green)"/>
  </svg>

  <div class="back-brand">
    <span class="brand-dot"></span>
    <span class="brand-name">CORVANE SUPPLY</span>
  </div>
</section>

</body>
</html>
```